I require a complete design for a responsive 3 page business website.

High end design type, similar to (in order of preference):
]https://brennalofts.co/
https://renewing-pathways-guidance.com.au/
https://quietridgementoring.com.au/
https://buildakindday.com/
https://thecalmfieldguide.com/
https://www.dalekestrel.com/
https://thepivot.com/

Please use the attached old company logo, which is to be used a reference for the new branding and design.

Please use the colour palette below
#3D3D3D
#FBF8F3
#CAAD53
#7EB492
#EDCFBF
Updates

Provided feedback to top 3 designs, now waiting on amended iterations.

Target Market(s)

Male & female 30-50s, small business owners and executive corporates, first world english speaking nations.

Industry/Entity Type

Life Coaching

Logo Text

Willow Compass Path. Tagline: Holistic Transformational Coaching

Number of Pages Required

3 page

Font styles to use
Sans Serif

Requirements
Must have
• Testimonials section, google reivews section, book online button.

```html
<!DOCTYPE html>
<html lang="en">
<head>
<meta charset="utf-8">
<title>Lumenrise — Willow Compass Path Transformational Life Coaching</title>
<link rel="stylesheet" href="https://fonts.googleapis.com/css2?family=Cinzel:wght@400;500;600&family=Poppins:ital,wght@0,300;0,400;0,500;0,700;0,800;1,300;1,400&display=swap">
<style>
:root{
  --ink:#3D3D3D;
  --cream:#FBF8F3;
  --gold:#CAAD53;
  --green:#7EB492;
  --green-deep:#6a9f7e;
  --peach:#EDCFBF;
  --peach-deep:#e2b39c;
  --white:#ffffff;
  --muted:#6b6b6b;
}
*{box-sizing:border-box;margin:0;padding:0}
html,body{width:1200px;height:4773px;overflow:hidden}
body{position:relative;background:var(--white);color:var(--ink);font-family:"Poppins",Arial,sans-serif;font-size:12px;line-height:1.6}
.abs{position:absolute}
.serif{font-family:"Cinzel",Georgia,serif}
.section-title{font-family:"Cinzel",Georgia,serif;color:var(--gold);font-weight:500;font-size:32px;letter-spacing:1px;line-height:1.15;text-align:center}

/* pill button */
.pill{position:absolute;display:flex;align-items:center;justify-content:space-between;gap:10px;height:42px;border-radius:21px;padding:0 4px 0 20px;font-family:"Cinzel",Georgia,serif;font-size:14px;letter-spacing:.8px;line-height:1;white-space:nowrap;color:var(--white);background:var(--green)}
.pill.gold{background:var(--gold)}
.pill .dot{flex:0 0 34px;width:34px;height:34px;border-radius:50%;background:var(--white);display:flex;align-items:center;justify-content:center}
.pill .dot i{display:block;width:16px;height:16px;border-radius:50%;border:2px solid var(--gold)}

/* header */
.site-header{position:absolute;left:0;top:0;width:1200px;height:70px;background:var(--white)}
.brand-name{position:absolute;left:64px;top:8px;font-family:"Cinzel",Georgia,serif;font-size:30px;color:var(--gold);line-height:1}
.brand-tag{position:absolute;left:65px;top:41px;font-size:7.5px;letter-spacing:1.2px;color:var(--gold);text-transform:uppercase}
.main-nav{position:absolute;left:436px;top:26px;display:flex;gap:17px;font-size:12px;text-transform:uppercase;color:var(--ink)}
.main-nav .active{color:var(--gold)}

/* hero */
.hero{position:absolute;left:0;top:70px;width:1200px;height:642px;background:linear-gradient(180deg,#3c3d58 0%,#8c6a70 28%,#e0a868 46%,#a9563f 62%,#5b2a22 80%,#3a1f1a 100%)}
.hero h1{position:absolute;left:61px;top:188px;font-size:42px;font-weight:800;color:var(--white);line-height:1.17;letter-spacing:.2px;text-transform:uppercase}
.hero .underline{position:absolute;left:61px;top:378px;width:336px;height:5px;background:var(--gold)}
.socials{position:absolute;display:flex;gap:6px}
.socials span{width:34px;height:34px;border-radius:50%;border:1.5px solid var(--white);display:block}

/* about */
.about-frame{position:absolute;left:204px;top:809px;width:329px;height:361px;border:7px solid var(--peach)}
.about-photo{position:absolute;left:178px;top:839px;width:328px;height:352px;background:linear-gradient(160deg,#9b4a3a,#c9a38c 45%,#e7ddd2 70%,#8a6c58)}
.about-text{position:absolute;left:612px;top:856px;width:380px}
.about-text h2{font-family:"Cinzel",Georgia,serif;color:var(--gold);font-weight:500;font-size:32px;letter-spacing:1px;line-height:1.2;margin-bottom:10px}
.about-text .lead{font-size:13.5px;line-height:1.55;margin-bottom:10px}
.about-text p{font-size:11px;line-height:1.75;color:var(--ink);margin-bottom:6px}
.about-text .sign{font-style:italic;color:var(--green);font-size:15px;margin-top:8px}

/* services */
.services-bg{position:absolute;left:0;top:1222px;width:1200px;height:620px;background:radial-gradient(ellipse at 50% 35%,#d8d8d8 0%,#ececec 35%,#fafafa 70%,#fff 100%)}
.service-sub{position:absolute;left:340px;top:1430px;width:520px;text-align:center;font-style:italic;font-size:13.5px;line-height:1.6}
.svc{position:absolute;text-align:center;width:240px;font-family:"Cinzel",Georgia,serif;font-size:15px;font-weight:500;line-height:1.35;color:var(--ink)}
.svc-photo{position:absolute;border-radius:50%;border:4px solid var(--green)}
.svc-feature{position:absolute;left:470px;top:1524px;width:260px;height:260px;border-radius:50%;background:var(--green);border:5px solid var(--gold);color:var(--white);text-align:center;padding:48px 30px 0}
.svc-feature h3{font-family:"Cinzel",Georgia,serif;font-weight:500;font-size:16px;line-height:1.4;margin-bottom:8px}
.svc-feature p{font-size:10.5px;line-height:1.75}
.svc-feature .go{width:32px;height:32px;border-radius:50%;background:var(--gold);margin:12px auto 0;display:flex;align-items:center;justify-content:center}

/* review strip */
.review-box{position:absolute;left:246px;top:2117px;width:710px;height:186px;border:2px solid var(--peach);border-radius:14px}
.review-box .inner{position:absolute;left:6px;top:6px;right:6px;bottom:6px;border:1.5px solid var(--gold);border-radius:10px;opacity:.6}
.review-brand{position:absolute;left:58px;top:52px;font-family:"Poppins",Arial,sans-serif;font-size:34px;font-weight:500;color:var(--ink);line-height:1}
.review-brand + .stars{position:absolute;left:58px;top:100px;font-size:18px;color:var(--gold);letter-spacing:2px}
.review-quote{position:absolute;left:305px;top:40px;width:345px;font-size:11.5px;line-height:1.85}
.review-quote .q{font-family:"Cinzel",Georgia,serif;color:var(--gold);font-size:30px;line-height:0;vertical-align:-8px}
.client{font-family:"Cinzel",Georgia,serif;color:var(--gold);font-size:15px;letter-spacing:1px}
.client::before{content:"";display:inline-block;width:18px;height:2px;background:var(--gold);vertical-align:middle;margin-right:10px}

/* testimonials */
.testimonials{position:absolute;left:0;top:2393px;width:1200px;height:411px}
.testi-text{position:absolute;left:726px;top:68px;width:410px;color:var(--white)}
.testi-text h2{font-family:"Cinzel",Georgia,serif;font-weight:500;font-size:33px;letter-spacing:1px;margin-bottom:18px}
.testi-text .q{font-family:"Cinzel",Georgia,serif;font-size:70px;line-height:.6;height:44px}
.testi-text p{font-size:12px;line-height:1.75;margin-bottom:14px}
.testi-text .client{color:var(--white)}
.testi-text .client::before{background:var(--white)}

/* blog */
.blog{position:absolute;left:0;top:2804px;width:1200px;height:668px;background:var(--cream)}
.blog-sub{position:absolute;left:0;top:120px;width:1200px;text-align:center;font-size:13.5px}
.card{position:absolute;top:178px;width:288px;height:418px;background:var(--white);border:1px solid #eee4d6;border-radius:10px;box-shadow:0 4px 14px rgba(0,0,0,.04)}
.card .img{position:absolute;left:6px;top:5px;width:276px;height:190px}
.card h3{position:absolute;left:16px;top:232px;font-family:"Cinzel",Georgia,serif;font-weight:500;font-size:15px;letter-spacing:.5px}
.card p{position:absolute;left:16px;top:262px;width:254px;font-size:10.5px;line-height:1.9;color:var(--muted)}

/* success stories */
.story-photo{position:absolute;left:167px;top:3621px;width:600px;height:398px;background:linear-gradient(120deg,#6a4a3a,#a87a5a 35%,#d9b890 60%,#8a6a4a)}
.story-card{position:absolute;left:665px;top:3685px;width:360px;height:270px;background:var(--white);box-shadow:0 6px 22px rgba(0,0,0,.1);padding:32px 40px}
.story-card .avatar{position:absolute;left:40px;top:34px;width:50px;height:50px;border-radius:50%;background:linear-gradient(135deg,#e6c8aa,#b88b6b)}
.story-card .who{position:absolute;left:108px;top:38px}
.story-card .who b{display:block;font-family:"Cinzel",Georgia,serif;font-weight:500;color:var(--green);font-size:15px;letter-spacing:.5px;line-height:1.2}
.story-card .who span{font-size:11.5px}
.story-card p{position:absolute;left:40px;top:110px;width:290px;font-size:11px;line-height:1.9;color:var(--muted)}
.story-card .more{position:absolute;right:52px;bottom:22px;font-family:"Cinzel",Georgia,serif;color:var(--gold);font-size:13px;text-decoration:underline}
.dots{position:absolute;left:912px;top:3979px;display:flex;gap:5px}
.dots i{display:block;width:9px;height:9px;border-radius:50%;background:#d9d9d9}
.dots i.on{background:var(--green)}

/* cta */
.cta-text{position:absolute;left:0;top:4212px;width:1200px;text-align:center;color:var(--white)}
.cta-text h2{font-family:"Cinzel",Georgia,serif;font-weight:500;font-size:35px;line-height:1.1;letter-spacing:1px}
.cta-text p{font-size:13.5px;line-height:1.65;margin-top:14px}

/* footer */
.site-footer{position:absolute;left:0;top:4463px;width:1200px;height:271px;background:var(--cream)}
.foot-col h4{font-family:"Cinzel",Georgia,serif;font-weight:500;color:var(--gold);font-size:14px;letter-spacing:1px}
.contact-row{position:absolute;display:flex;align-items:flex-start;gap:14px;font-size:11.5px;line-height:1.7}
.quick-links{position:absolute;left:650px;top:98px;font-size:11.5px;display:flex;gap:8px}
.copyright{position:absolute;left:0;top:4734px;width:1200px;height:39px;background:var(--green);color:var(--white);text-align:center;font-size:11.5px;line-height:39px}
</style>
</head>
<body>

<!-- Header -->
<header class="site-header">
  <div class="brand-name">Lumenrise</div>
  <div class="brand-tag">Transformational Life Coaching</div>
  <nav class="main-nav">
    <span class="active">Home</span><span>About Me</span><span>Life Coaching Sevices</span><span>Success Stories</span><span>Blog</span><span>Contact</span>
  </nav>
  <div class="abs" style="left:450px;top:50px;width:8px;height:8px;border-radius:50%;border:1.5px solid var(--gold)"></div>
  <a class="pill" style="left:976px;top:14px;width:164px">BOOK NOW<span class="dot"><i></i></span></a>
</header>

<!-- Hero -->
<section class="hero" role="img" aria-label="Sunset meadow of red flowers with a heart-shaped red tree">
  <h1>Willow Compass<br>Path<br>Tranformational<br>Life Coaching</h1>
  <div class="underline"></div>
  <a class="pill" style="left:61px;top:402px;width:164px">BOOK NOW<span class="dot"><i></i></span></a>
  <div class="socials" style="left:1029px;top:592px" aria-label="Social links"><span></span><span></span><span></span></div>
</section>
<div class="abs" style="left:584px;top:694px;width:32px;height:32px;border-radius:50%;background:var(--white);border:2px solid var(--gold)"></div>

<!-- About -->
<div class="about-frame"></div>
<div class="about-photo" role="img" aria-label="Portrait of a smiling coach holding a tablet"></div>
<div class="about-text">
  <h2>About Me</h2>
  <div class="lead">Lorem Ipsum has been the industry's standard text ever since the, when an unknown printer took.</div>
  <p>Lorem Ipsum has been the industry's standard dummy text ever since the, when an unknown printer took a galley of type and scrambled it to make a type specimen book.</p>
  <p>Lorem Ipsum has been the industry's standard dummy text ever since the 1500s, when an unknown printer took a galley of type and scrambled it to make a type specimen book. It has survived not only five centuries, but also the leap into electronic typesetting, remaining essentially unchanged.</p>
  <div class="sign">Transformational Life Coaching</div>
</div>
<a class="pill" style="left:612px;top:1185px;width:164px">BOOK NOW<span class="dot"><i></i></span></a>

<!-- Services -->
<div class="services-bg" role="img" aria-label="Faded photo of a woman with open arms in a meadow"></div>
<h2 class="section-title abs" style="left:0;top:1340px;width:1200px">Life Coaching<br>Sevices</h2>
<p class="service-sub">Lorem ipsum has been the industry's standard dummy text ever since the, when an unknown printer took a galley.</p>
<svg class="abs" style="left:0;top:1470px" width="1200" height="200" viewBox="0 0 1200 200">
  <path d="M0 14 Q600 280 1200 14" fill="none" stroke="var(--green)" stroke-width="10"/>
  <path d="M0 30 Q600 296 1200 30" fill="none" stroke="#ffffff" stroke-width="4"/>
</svg>
<div class="svc-photo" style="left:221px;top:1556px;width:140px;height:140px;background:linear-gradient(160deg,#cfe3f0,#9fb7c9 60%,#c8a58a)" role="img" aria-label="Woman in a yoga balance pose"></div>
<div class="svc" style="left:171px;top:1718px">Healthy Mind and<br>Body Life Coaching</div>
<div class="svc-feature">
  <h3>Life Coaching<br>Consultation</h3>
  <p>Lorem ipsum has been the industry's standard dummy text ever since the when an unknown printer took a galley of type scrambled</p>
  <div class="go"><svg width="16" height="16" viewBox="0 0 16 16"><path d="M3 8h10M9 4l4 4-4 4" stroke="#fff" stroke-width="2" fill="none"/></svg></div>
</div>
<div class="svc-photo" style="left:841px;top:1556px;width:140px;height:140px;background:linear-gradient(160deg,#f1f1f1,#d7cfc6 55%,#6d6a66)" role="img" aria-label="Coach presenting to a seated group"></div>
<div class="svc" style="left:791px;top:1718px">Career Analysis Life<br>Coaching</div>

<div class="svc-photo" style="left:221px;top:1841px;width:140px;height:140px;background:linear-gradient(160deg,#eaeaea,#bdbdbd 55%,#555)" role="img" aria-label="Stressed man on two telephones"></div>
<div class="svc" style="left:171px;top:2003px">Mind Your Behaviour<br>Life Coaching</div>
<div class="svc-photo" style="left:530px;top:1841px;width:140px;height:140px;background:linear-gradient(160deg,#efe7df,#caa98a 55%,#8e6f55)" role="img" aria-label="Woman working on a laptop at home"></div>
<div class="svc" style="left:480px;top:2003px">Online Life<br>Coaching</div>
<div class="svc-photo" style="left:834px;top:1841px;width:140px;height:140px;background:linear-gradient(160deg,#e8e8e8,#b98a6a 50%,#3b2a22)" role="img" aria-label="Woman holding a smile drawing over her mouth"></div>
<div class="svc" style="left:784px;top:2003px">Hypnosis for Anxiety,<br>Addictions &amp; Habits</div>

<!-- Review strip -->
<svg class="abs" style="left:178px;top:2192px" width="20" height="30" viewBox="0 0 20 30"><path d="M16 2 4 15l12 13" fill="none" stroke="#888" stroke-width="2"/></svg>
<svg class="abs" style="left:1010px;top:2192px" width="20" height="30" viewBox="0 0 20 30"><path d="M4 2l12 13L4 28" fill="none" stroke="#555" stroke-width="2"/></svg>
<div class="review-box">
  <div class="inner"></div>
  <div class="review-brand">Starlit</div>
  <div class="stars">★★★★★</div>
  <div class="review-quote">
    <span class="q">“</span> Lorem Ipsum has been the industry's standard dummy text ever since the 1500s, when an unknown printer took a galley of type and scrambled make <span class="q">”</span>
    <div class="client" style="margin-top:12px">Client Name</div>
  </div>
</div>

<!-- Testimonials -->
<section class="testimonials">
  <svg class="abs" style="left:0;top:0" width="1200" height="411" viewBox="0 0 1200 411">
    <defs>
      <linearGradient id="peach" x1="0" y1="0" x2="1" y2="0">
        <stop offset="0" stop-color="#e2ab90"/><stop offset="1" stop-color="#efd3c4"/>
      </linearGradient>
      <linearGradient id="face" x1="0" y1="0" x2="1" y2="1">
        <stop offset="0" stop-color="#5d6a52"/><stop offset=".45" stop-color="#b98c6e"/><stop offset="1" stop-color="#3d2c24"/>
      </linearGradient>
    </defs>
    <rect width="1200" height="411" fill="url(#peach)"/>
    <path d="M382 0 H470 C430 120 470 260 540 411 H420 C370 280 350 120 382 0Z" fill="var(--gold)"/>
    <path d="M430 0 H510 C470 130 540 300 640 411 H560 C480 290 420 140 430 0Z" fill="var(--green)"/>
    <path d="M0 0 H432 C410 140 470 300 560 411 H0Z" fill="url(#face)" role="img" aria-label="Laughing woman with flowing dark hair"/>
    <path d="M470 0 H500 C470 150 560 320 660 411 H610 C520 310 455 150 470 0Z" fill="#ffffff"/>
  </svg>
  <div class="testi-text">
    <h2>Testimonials</h2>
    <div class="q">“</div>
    <p>" Lorem Ipsum has been the industry's standard dummy text ever since the when an unknown printer took a galley of type and scrambled it to make a type specimen book. It has survived not only five centuries, but also the leap into electronic."</p>
    <div class="client">Client Name</div>
  </div>
  <svg class="abs" style="left:1088px;top:370px" width="40" height="24" viewBox="0 0 40 24"><path d="M12 2 3 12l9 10" fill="none" stroke="var(--gold)" stroke-width="2"/><path d="M26 2l9 10-9 10" fill="none" stroke="#fff" stroke-width="2"/></svg>
</section>

<!-- Blog -->
<section class="blog">
  <h2 class="section-title abs" style="left:0;top:76px;width:1200px">Blog Post</h2>
  <div class="blog-sub">Lorem Ipsum has been the industry's standard</div>

  <article class="card" style="left:144px">
    <div class="img" role="img" aria-label="Woman with open arms in a sunny field" style="background:linear-gradient(180deg,#bcd3e6,#a9b98c 55%,#6f7f55)"></div>
    <h3>LOREM IPSUM INDUSTRY</h3>
    <p>Lorem Ipsum has been the industry's THE standard dummy text ever since the, when an unknown printer took a galley of type and scrambled it to make.</p>
    <a class="pill" style="left:16px;top:345px;width:166px">LEARN MORE<span class="dot"><i></i></span></a>
  </article>
  <article class="card" style="left:457px">
    <div class="img" role="img" aria-label="Two heart shapes made of colourful blocks on wooden boards" style="background:linear-gradient(180deg,#f2f2f0,#d9d7d2)"></div>
    <h3>LOREM IPSUM INDUSTRY</h3>
    <p>Lorem Ipsum has been the industry's THE standard dummy text ever since the, when an unknown printer took a galley of type and scrambled it to make.</p>
    <a class="pill gold" style="left:16px;top:345px;width:166px">LEARN MORE<span class="dot"><i></i></span></a>
  </article>
  <article class="card" style="left:770px">
    <div class="img" role="img" aria-label="Profile silhouette filled with glowing golden light" style="background:linear-gradient(135deg,#2e3a6a,#6a5a9a 40%,#d6a24a 75%,#3a2a1a)"></div>
    <h3>LOREM IPSUM INDUSTRY</h3>
    <p>Lorem Ipsum has been the industry's THE standard dummy text ever since the, when an unknown printer took a galley of type and scrambled it to make.</p>
    <a class="pill" style="left:16px;top:345px;width:166px">LEARN MORE<span class="dot"><i></i></span></a>
  </article>
</section>

<!-- Success stories -->
<h2 class="section-title abs" style="left:0;top:3542px;width:1200px">Success Stories</h2>
<div class="story-photo" role="img" aria-label="Two women embracing and laughing"></div>
<div class="story-card">
  <div class="avatar" role="img" aria-label="Client portrait"></div>
  <div class="who"><b>MARA QUINLAN</b><span>something.com</span></div>
  <p>Lorem Ipsum has been the industry's standard dummy text ever since the 1500s, when an this unknown printer took a galley of type and that scrambled make text print Lorem Ipsum has been the industry's standard dummy.</p>
  <div class="more">READ MORE ▸</div>
</div>
<div class="dots"><i></i><i></i><i></i><i></i><i class="on"></i><i></i><i></i><i></i></div>

<!-- CTA -->
<svg class="abs" style="left:0;top:4080px" width="1200" height="384" viewBox="0 0 1200 384" role="img" aria-label="Green hillside landscape">
  <defs><linearGradient id="hill" x1="0" y1="0" x2="0" y2="1"><stop offset="0" stop-color="#6e9c7c"/><stop offset="1" stop-color="#5f8f6c"/></linearGradient></defs>
  <path d="M0 190 Q600 -60 1200 190 V384 H0Z" fill="url(#hill)"/>
  <path d="M0 180 Q600 -72 1200 180" fill="none" stroke="var(--green)" stroke-width="6"/>
</svg>
<div class="cta-text">
  <h2>Request a Free<br>Consultation</h2>
  <p>If you have an any Question Willow Compass Path<br>Transformational Life Coaching</p>
</div>
<a class="pill gold" style="left:517px;top:4350px;width:164px">BOOK NOW<span class="dot"><i></i></span></a>

<!-- Footer -->
<footer class="site-footer">
  <div class="brand-name" style="left:60px;top:46px;font-size:28px">Lumenrise</div>
  <div class="brand-tag" style="left:61px;top:78px">Transformational Life Coaching</div>
  <div class="abs" style="left:136px;top:97px;width:26px;height:26px;border-radius:50%;border:2px solid var(--gold)"></div>
  <p class="abs" style="left:61px;top:142px;width:250px;font-size:10.5px;line-height:1.85">Lorem Ipsum has been the industry's The standard dummy text ever since the, when an unknown printer took a galley.</p>
  <div class="abs serif" style="left:61px;top:205px;color:var(--gold);font-size:13px">READ MORE</div>

  <div class="foot-col abs" style="left:372px;top:46px"><h4>CONTACT INFO</h4></div>
  <div class="contact-row" style="left:372px;top:88px">
    <svg width="26" height="26" viewBox="0 0 26 26"><path d="M13 3a7 7 0 0 0-7 7c0 6 7 13 7 13s7-7 7-13a7 7 0 0 0-7-7z" fill="none" stroke="var(--gold)" stroke-width="1.5"/><circle cx="13" cy="10" r="2.5" fill="none" stroke="var(--gold)" stroke-width="1.5"/></svg>
    <span>101 - Lorem Ipsum has been<br>the industry's</span>
  </div>
  <div class="contact-row" style="left:372px;top:150px">
    <svg width="26" height="22" viewBox="0 0 26 22"><path d="M6 3l4 0 2 5-3 2c1 3 3 5 6 6l2-3 5 2v4c0 1-1 2-2 2C10 21 3 14 3 5c0-1 1-2 3-2z" fill="none" stroke="var(--gold)" stroke-width="1.5"/></svg>
    <span>+1 555 204 7718</span>
  </div>
  <div class="contact-row" style="left:372px;top:188px">
    <svg width="26" height="20" viewBox="0 0 26 20"><rect x="2" y="3" width="22" height="15" fill="none" stroke="var(--gold)" stroke-width="1.5"/><path d="M2 3l11 9 11-9" fill="none" stroke="var(--gold)" stroke-width="1.5"/></svg>
    <span>info@lumenrise.com</span>
  </div>

  <div class="foot-col abs" style="left:648px;top:46px"><h4>QUICK LINKS</h4></div>
  <div class="quick-links" style="top:83px">
    <span>Home</span><span>|</span><span>About Me</span><span>|</span><span>Life Coaching Sevices</span><span>|</span><span>Success Stories</span><span>|</span><span>Blog</span><span>|</span><span>Contact</span>
  </div>
  <div class="foot-col abs" style="left:648px;top:128px"><h4>FOLLOW US</h4></div>
  <div class="abs" style="left:648px;top:163px;display:flex;gap:8px" aria-label="Social links">
    <span style="width:36px;height:36px;border-radius:50%;background:#3b5a9a"></span>
    <span style="width:36px;height:36px;border-radius:50%;background:#2c9be0"></span>
    <span style="width:36px;height:36px;border-radius:50%;background:#c2378a"></span>
  </div>
</footer>
<div class="copyright">©LUMENRISE Tranformational Life Coaching - 2021 All rights reserved.</div>

</body>
</html>
```